Global Harbor Learning Network

Our company needs a simple effective website with a clean design. We are working towards lowering the number of drownings that effect huge numbers each year. We will primarily link members to find education seminars, conferences and online material. With a forum to pose questions, have them answered by the community and moderated by staff members.

Target Market(s)

Swimming School Owners, Coaches, Parents and Community Groups

Industry/Entity Type

Education

Number of Pages Required

5+ page

Requirements
Must have
• A layout for all of the included pages. A good design for the forum. I will need to send this concept design to a coder for the final product.
Nice to have
• i would like to see an Olympic Swimming Pool incorporated into the options menu.

```html
<!DOCTYPE html>
<html lang="en">
<head>
<meta charset="utf-8">
<title>Why Become Involved – Global Harbor Learning Network</title>
<link href="https://fonts.googleapis.com/css2?family=Comfortaa:wght@300&family=Nunito+Sans:wght@400&display=swap" rel="stylesheet">
<style>
  :root {
    --page-navy: #0c2f60;
    --page-deep: #082449;
    --page-mid: #1d4f8c;
    --side-blue: #05a5e6;
    --nav-blue: #1fc2f6;
    --nav-line: #12aee6;
    --white: #ffffff;
    --active-text: #1aa9e4;
    --footer-band: #0a2a55;
    --footer-text: #6c8cbd;
    --photo-top: #5fb3e6;
    --photo-bottom: #1f5fc4;
    --globe-top: #8cc8ee;
    --globe-bottom: #2d74c2;
  }
  * { box-sizing: border-box; margin: 0; padding: 0; }
  html, body { width: 1200px; height: 938px; overflow: hidden; }
  body { position: relative; font-family: "Nunito Sans", sans-serif; color: var(--white); background: var(--page-navy); }

  .backdrop {
    position: absolute; inset: 0;
    background:
      radial-gradient(ellipse 420px 520px at 470px 430px, rgba(60,110,170,.55), transparent 70%),
      radial-gradient(ellipse 300px 380px at 1000px 520px, rgba(40,90,160,.45), transparent 70%),
      linear-gradient(180deg, var(--page-mid) 0%, var(--page-navy) 55%, var(--page-deep) 100%);
  }

  .sidebar { position: absolute; left: 66px; top: 0; width: 247px; height: 880px; }
  .sidebar-shape { position: absolute; left: 0; top: 0; }
  .brand {
    position: absolute; left: 0; top: 0; width: 247px; height: 248px;
    display: flex; flex-direction: column; align-items: center; justify-content: center; gap: 14px;
  }
  .brand-mark { width: 30px; height: 30px; border-radius: 50%; background: var(--white); }
  .brand-name { font-size: 22px; line-height: 1.25; text-align: center; color: var(--white); width: 190px; }

  .nav { position: absolute; left: 0; top: 248px; width: 247px; list-style: none; }
  .nav-item {
    position: relative; height: 47.8px; display: flex; align-items: center;
    background: var(--nav-blue); border-bottom: 1px solid var(--nav-line);
    font-size: 18px; color: var(--white);
  }
  .nav-item svg { position: absolute; left: 21px; width: 24px; height: 24px; }
  .nav-item span { position: absolute; left: 76px; }
  .nav-item.is-active { background: transparent; border-bottom-color: transparent; color: var(--active-text); }

  .globe-art {
    position: absolute; left: 61px; top: 670px; width: 132px; height: 192px;
    background: linear-gradient(180deg, var(--globe-top) 0%, var(--globe-bottom) 100%);
  }

  .content { position: absolute; left: 357px; top: 0; }
  .page-title {
    position: absolute; left: 0; top: 28px; white-space: nowrap;
    font-family: "Comfortaa", sans-serif; font-weight: 300; font-size: 49px; letter-spacing: -1px;
  }
  .copy { position: absolute; left: 2px; top: 117px; width: 395px; font-size: 17px; line-height: 29px; }
  .copy p + p { margin-top: 29px; }

  .feature-photo {
    position: absolute; left: 797px; top: 125px; width: 337px; height: 540px;
    background: linear-gradient(180deg, var(--photo-top) 0%, #3b8ad8 45%, var(--photo-bottom) 100%);
  }

  .footer {
    position: absolute; left: 0; bottom: 0; width: 1200px; height: 45px;
    background: var(--footer-band); display: flex; align-items: center; justify-content: center;
    font-size: 14px; color: var(--footer-text);
  }
</style>
</head>
<body>
  <div class="backdrop" role="img" aria-label="Faded underwater photo of a swim instructor with a child"></div>

  <aside class="sidebar">
    <svg class="sidebar-shape" width="247" height="880" viewBox="0 0 247 880">
      <path d="M0 0 H247 V780 L206 792 C206 840 170 876 124 876 C78 876 42 840 42 792 L0 780 Z" fill="var(--side-blue)"/>
    </svg>

    <div class="brand">
      <div class="brand-mark"></div>
      <div class="brand-name">Global Harbor Learning Network</div>
    </div>

    <ul class="nav">
      <li class="nav-item">
        <svg viewBox="0 0 24 24" fill="#fff"><path d="M12 3 2 12h3v8h5v-5h4v5h5v-8h3z"/></svg>
        <span>Welcome</span>
      </li>
      <li class="nav-item">
        <svg viewBox="0 0 24 24" fill="#fff"><circle cx="12" cy="8" r="3.5"/><circle cx="5" cy="10" r="2.5"/><circle cx="19" cy="10" r="2.5"/><path d="M5 20c0-4 3-7 7-7s7 3 7 7z"/><path d="M0 19c0-3 2-5 5-5 1 0 1.5.2 2 .5C5.5 16 5 17.5 5 19z"/><path d="M24 19c0-3-2-5-5-5-1 0-1.5.2-2 .5 1.5 1.5 2 3 2 4.5z"/></svg>
        <span>About Us</span>
      </li>
      <li class="nav-item">
        <svg viewBox="0 0 24 24" fill="#fff"><path d="M1 8h5l4-2 4 2 3-1h6v7h-3l-5 4-2-1-2 1-4-3H1z"/></svg>
        <span>Community</span>
      </li>
      <li class="nav-item">
        <svg viewBox="0 0 24 24" fill="none" stroke="#fff" stroke-width="2"><rect x="3" y="4" width="18" height="17" rx="1"/><path d="M3 9h18M8 2v4M16 2v4"/></svg>
        <span>Events</span>
      </li>
      <li class="nav-item is-active">
        <svg class="active-tab" viewBox="0 0 290 48" style="width:290px;height:48px;left:-10px;top:0;"><path d="M0 0 H277 L290 24 L277 48 H0 Z" fill="#fff"/></svg>
        <svg viewBox="0 0 24 24"><circle cx="12" cy="12" r="11" fill="var(--active-text)"/><text x="12" y="17" text-anchor="middle" font-size="14" font-family="Nunito Sans, sans-serif" fill="#fff">?</text></svg>
        <span>Why Get Involved</span>
      </li>
      <li class="nav-item">
        <svg viewBox="0 0 24 24" fill="none" stroke="#fff" stroke-width="2"><path d="M5 2h11l3 3v12H5z"/><path d="M8 7h7M8 11h7"/><circle cx="16" cy="18" r="3"/></svg>
        <span>Become Certified</span>
      </li>
      <li class="nav-item">
        <svg viewBox="0 0 24 24" fill="none" stroke="#fff" stroke-width="2.2"><path d="M10 4h10v16H10"/><path d="M2 12h12M10 8l4 4-4 4"/></svg>
        <span>Log In</span>
      </li>
      <li class="nav-item">
        <svg viewBox="0 0 24 24" fill="#fff"><path d="M1 5h22v14H1z"/><path d="M1 5l11 8 11-8" fill="none" stroke="var(--nav-blue)" stroke-width="2"/></svg>
        <span>Contact Us</span>
      </li>
    </ul>

    <div class="globe-art" role="img" aria-label="Illustration of a water drop holding a globe"></div>
  </aside>

  <main class="content">
    <h1 class="page-title">Why Become Involved</h1>
    <div class="copy">
      <p>The best way to provide education is in a safe controlled environment. Running your own facility is a rewarding lifelong move into business. Provid&shy;ing a community service with an opportunity to work with a passionate and driven community. Become a leader in educating children to be safe around water.</p>
      <p>Creating a purpose built facility can be tough. Having a good heart is a great start, but misinfor&shy;mation can be just as dangerous as no informa&shy;tion. Your good intentions need to be directed ef&shy;fectively.</p>
      <p>The most important asset is great coaches and a top notch pool. Luckily the industry has been around for a long time and has produced some excellent models that you can follow.</p>
      <p>With many countries having turn key consulting to help you on your way.</p>
    </div>
  </main>

  <div class="feature-photo" role="img" aria-label="Underwater photo of an instructor holding a baby in a pool"></div>

  <footer class="footer">© 2016 Global Harbor Learning Network. All Rights Reserved.</footer>
</body>
</html>
```